Identidad Corporativa / Corporate Identity for Proposal Document

Crear una identidad corporativa para una propuesta de negocio. El documento debe estar dividió en Portada, Carta de Presentación, Contenido, Perfil Corporativo, Vision, Misión, Nuestros Servicios, Situación actual en el cliente, Nuestras Recomendaciones, Metodología de trabajo, Propuesta de Negocio, Términos de Pago, Aceptación del Propuesta. Proveer documento en formato Word.

Create a corporate Identity for a Business Proposal Standard. The table of contest will have Cover, Presentation Letter, Table of Content, Corporate Info, Vision, Mission, Our Services, Customer Situation, Our Recommendations, Methodology of Work, Business Proposal, Payment Terms, Acceptance.

Provide document Word format.

```html
<!DOCTYPE html>
<html lang="es">
<head>
<meta charset="utf-8">
<title>Propuesta de Consultoría – Clearpath Systems</title>
<link href="https://fonts.googleapis.com/css2?family=Josefin+Sans:ital,wght@0,300;0,400;0,600;0,700;1,600;1,700&family=Montserrat:wght@500;600&display=swap" rel="stylesheet">
<style>
  :root{
    --canvas:#ececec;
    --paper:#ffffff;
    --navy:#1f2a86;
    --blue:#2c3db8;
    --deep:#0d1656;
    --green:#8fd11f;
    --ink:#2a2a2a;
    --muted:#dcdcdc;
  }
  *{margin:0;padding:0;box-sizing:border-box}
  html,body{width:1200px;height:531px;overflow:hidden;background:var(--canvas)}
  body{position:relative;font-family:"Josefin Sans",sans-serif;color:var(--ink)}
  .page{position:absolute;top:33px;width:350px;height:454px;background:var(--paper);overflow:hidden}
  .page--cover{left:53px}
  .page--letter{left:418px}
  .page--profile{left:785px}

  /* brand name */
  .brand{display:flex;align-items:center;gap:5px;font-weight:700;color:var(--navy);font-size:13px;letter-spacing:.2px;white-space:nowrap}
  .brand__dot{width:10px;height:10px;border-radius:50%;background:var(--green);flex:none}

  /* cover */
  .cover__hero{position:absolute;left:0;top:0;width:350px;height:310px;
    background:radial-gradient(ellipse at 60% 35%,#3a63e8 0%,#1d37b8 35%,#0b1662 75%,#070d3d 100%)}
  .cover__curve{position:absolute;left:0;top:215px;width:350px;height:110px}
  .cover__base{position:absolute;left:0;top:300px;width:350px;height:154px;background:linear-gradient(#fff 0%,#eeeeee 100%)}
  .cover__brand{position:absolute;top:330px;left:0;width:100%;display:flex;justify-content:center}
  .cover__dot{position:absolute;left:172px;width:6px;height:6px;border-radius:50%;background:var(--green)}
  .cover__title{position:absolute;top:391px;left:0;width:100%;text-align:center;font-family:"Montserrat",sans-serif;font-weight:500;color:var(--navy);font-size:12.5px;line-height:15px;text-transform:uppercase}

  /* shared header & waves */
  .page__header{position:absolute;top:22px;left:0;width:100%;display:flex;justify-content:center}
  .page__rule{position:absolute;top:52px;left:128px;width:94px;height:1.5px;background:var(--green)}
  .page__waves{position:absolute;left:0;bottom:0;width:350px;height:90px}

  /* letter */
  .letter{position:absolute;top:83px;left:30px;width:292px;font-size:10.5px;line-height:13px;font-weight:400}
  .letter p{margin-bottom:11px}
  .letter__sign{font-weight:600;margin-top:18px;margin-bottom:0 !important}

  /* profile */
  .profile__title{position:absolute;top:90px;left:18px;font-size:14px;font-weight:400;color:var(--ink)}
  .profile__text{position:absolute;top:115px;left:18px;width:315px;font-size:6.6px;line-height:8px}
  .profile__text p{margin-bottom:7px}
  .diagram{position:absolute;top:185px;left:0;width:350px;height:110px}
  .diagram__hub{position:absolute;left:18px;top:15px;width:80px;height:80px;border-radius:50%;background:var(--navy);border:4px solid var(--green);display:flex;align-items:center;justify-content:center}
  .diagram__hub .brand{color:#fff;font-size:8px;gap:3px}
  .diagram__hub .brand__dot{width:6px;height:6px}
  .diagram__lines{position:absolute;left:0;top:0;width:350px;height:110px}
  .pill{position:absolute;left:125px;width:212px;height:12px;border-radius:6px;font-size:6.4px;font-weight:600;display:flex;align-items:center;justify-content:center}
  .pill--green{background:var(--green);color:var(--navy)}
  .pill--navy{background:var(--navy);color:#fff}
  .mission{position:absolute;top:318px;left:20px;width:312px;text-align:center;font-size:8.4px;line-height:10px;font-style:italic;font-weight:700;color:var(--navy)}
  .mission__rule{position:absolute;top:356px;left:168px;width:14px;height:1px;background:var(--green)}
</style>
</head>
<body>

<!-- Cover -->
<section class="page page--cover">
  <div class="cover__hero" role="img" aria-label="Fotografía en tonos azules de una mano tocando iconos digitales de comunicación y dispositivos"></div>
  <div class="cover__base"></div>
  <svg class="cover__curve" viewBox="0 0 350 110" preserveAspectRatio="none" aria-hidden="true">
    <path d="M0 90 C90 40 240 30 350 55 L350 110 L0 110Z" fill="var(--green)"/>
    <path d="M0 95 C90 48 240 38 350 62 L350 110 L0 110Z" fill="#ffffff"/>
  </svg>
  <div class="cover__brand"><span class="brand"><span class="brand__dot"></span>Clearpath Systems</span></div>
  <span class="cover__dot" style="top:370px"></span>
  <h1 class="cover__title">Propuesta de Consultoría,<br>Mantenimiento y Desarrollo de Sistemas</h1>
  <span class="cover__dot" style="top:428px"></span>
</section>

<!-- Presentation letter -->
<section class="page page--letter">
  <div class="page__header"><span class="brand"><span class="brand__dot"></span>Clearpath Systems</span></div>
  <div class="page__rule"></div>
  <div class="letter">
    <p>De nuestra mayor consideración:</p>
    <p>Por la presente nos dirigimos a usted con la propuesta de Consultoría, Programación y Servicios.</p>
    <p>Clearpath Systems, Inc. provee toda su experiencia de más de 27 años en el área de sistemas de información y desarrollo de aplicaciones.</p>
    <p>Finalmente, le agradezco la oportunidad que nos brindan de presentarle nuestra propuesta.</p>
    <p>Atentamente,</p>
    <p class="letter__sign">Marco A. Ríos Valle<br>Presidente</p>
  </div>
  <svg class="page__waves" viewBox="0 0 350 90" preserveAspectRatio="none" aria-hidden="true">
    <path d="M0 90 C110 45 230 22 350 28 L350 90Z" fill="var(--green)"/>
    <path d="M0 18 C60 40 150 75 350 68 L350 90 L0 90Z" fill="var(--navy)"/>
  </svg>
</section>

<!-- Corporate profile -->
<section class="page page--profile">
  <div class="page__header"><span class="brand"><span class="brand__dot"></span>Clearpath Systems</span></div>
  <div class="page__rule"></div>
  <h2 class="profile__title">Perfil Corporativo</h2>
  <div class="profile__text">
    <p>Clearpath Systems Inc. empresa establecida desde 1990, brinda servicio en el área de sistemas de información.<br>
    En el mundo de los negocios hoy día la tecnología y el servicio son fundamental y vital para el éxito de la operación del negocio. Mantener un balance es esencial para competir en este ambiente tan dinámico. Implementado apropiadamente, un sistema de información adecuado ofrece a toda empresa la distinción sobre su competencia.</p>
    <p>Este reto es la razón de ser para Clearpath Systems, Inc.</p>
  </div>
  <div class="diagram">
    <svg class="diagram__lines" viewBox="0 0 350 110" aria-hidden="true">
      <g fill="none" stroke="var(--navy)" stroke-width="1">
        <path d="M95 40 L110 14 L125 14"/>
        <path d="M100 48 L112 35 L125 35"/>
        <path d="M102 56 L125 56"/>
        <path d="M100 64 L112 77 L125 77"/>
        <path d="M95 72 L110 98 L125 98"/>
      </g>
    </svg>
    <div class="diagram__hub"><span class="brand"><span class="brand__dot"></span>Clearpath</span></div>
    <div class="pill pill--green" style="top:8px">Compañía con más de 27 años de experiencia</div>
    <div class="pill pill--navy" style="top:29px">Soporte técnico, desarrollo de aplicaciones, consultoría</div>
    <div class="pill pill--green" style="top:50px">Provee soluciones para el manejo de información</div>
    <div class="pill pill--navy" style="top:71px">Soluciones es: Control + Confianza + Calidad</div>
    <div class="pill pill--green" style="top:92px">Innovación en la tecnología</div>
  </div>
  <p class="mission">La misión de nuestra compañía es proveer a nuestros clientes productos y servicios de la más alta calidad para el manejo y procesamiento de la información.</p>
  <div class="mission__rule"></div>
  <svg class="page__waves" viewBox="0 0 350 90" preserveAspectRatio="none" aria-hidden="true">
    <path d="M0 90 C110 45 230 22 350 28 L350 90Z" fill="var(--green)"/>
    <path d="M0 18 C60 40 150 75 350 68 L350 90 L0 90Z" fill="var(--navy)"/>
  </svg>
</section>

</body>
</html>
```